Verdant Loop Advisors, LLC

I am looking for a simple, clear layout with my logo prominent and embossed, on the best quality card stock available. I would like the business name and phone number included on the card as well......I dont want my name anywhere on the card and I would like my logo embossed on the card......something simple with a white back......open to designs as long as they go along with recycling symbols and green type stuff.....The address, website, cell number, fax number, and email are listed below

5374 Tillbury Fenwood Road
Hyattsville, MD 20785

c. 240.555.0143 f. 240.555.0187
e. sales@verdantloopadvisors.example
w. www.verdantloopadvisors.example

Industry/Entity Type

Recycling

```html
<!DOCTYPE html>
<html lang="en">
<head>
<meta charset="utf-8">
<title>Verdant Loop Advisors, LLC – Business Card</title>
<link rel="stylesheet" href="https://fonts.googleapis.com/css2?family=Ubuntu:wght@400;700&display=swap">
<style>
  :root {
    --page-bg: #ffffff;
    --card-blue: #3eaedb;
    --card-blue-deep: #2596c6;
    --card-blue-light: #6cc6ea;
    --swoosh: rgba(255, 255, 255, 0.14);
    --swoosh-on-white: rgba(62, 174, 219, 0.07);
    --card-white: #ffffff;
    --text-light: #ffffff;
    --text-blue: #1f86b4;
    --brand-green: #8cc63f;
    --card-shadow: rgba(0, 0, 0, 0.18);
  }
  * { box-sizing: border-box; margin: 0; padding: 0; }
  html, body {
    width: 1200px;
    height: 572px;
    overflow: hidden;
    background: var(--page-bg);
  }
  .canvas {
    position: relative;
    width: 1200px;
    height: 572px;
    display: flex;
    align-items: center;
    justify-content: center;
    gap: 60px;
  }
  .card {
    position: relative;
    width: 520px;
    height: 320px;
    border-radius: 20px;
    overflow: hidden;
    box-shadow: 0 6px 18px var(--card-shadow);
    font-family: "Ubuntu", sans-serif;
  }
  .card--front {
    background: linear-gradient(135deg, var(--card-blue-light) 0%, var(--card-blue) 45%, var(--card-blue-deep) 100%);
    color: var(--text-light);
  }
  .card--back {
    background: var(--card-white);
    color: var(--text-blue);
    border: 1px solid #e3eef4;
  }
  .card__swooshes {
    position: absolute;
    inset: 0;
    width: 100%;
    height: 100%;
  }
  /* Front */
  .brand {
    position: absolute;
    left: 44px;
    top: 136px;
    display: flex;
    align-items: center;
    gap: 12px;
  }
  .brand__mark {
    flex: 0 0 40px;
    width: 40px;
    height: 40px;
    border-radius: 50%;
    background: var(--brand-green);
  }
  .brand__name {
    font-weight: 700;
    font-size: 23px;
    letter-spacing: 0.3px;
    white-space: nowrap;
    line-height: 1;
    color: var(--text-light);
  }
  /* Back */
  .web-band {
    position: absolute;
    left: 0;
    right: 0;
    top: 78px;
    height: 60px;
    border-top: 3px solid var(--card-blue);
    border-bottom: 3px solid var(--card-blue);
    display: flex;
    align-items: center;
    justify-content: center;
  }
  .web-band__url {
    font-weight: 700;
    font-size: 18px;
    letter-spacing: 0.3px;
  }
  .contact {
    position: absolute;
    right: 28px;
    bottom: 34px;
    text-align: right;
    font-style: normal;
    font-size: 12.5px;
    line-height: 1.55;
  }
  .contact__address { margin-bottom: 14px; }
</style>
</head>
<body>
<main class="canvas">

  <section class="card card--front" aria-label="Card front">
    <svg class="card__swooshes" viewBox="0 0 520 320" aria-hidden="true">
      <path d="M-20 230 C 120 120, 320 60, 560 110 L 560 -20 L -20 -20 Z" fill="var(--swoosh)"/>
      <path d="M-20 300 C 160 200, 360 180, 560 240 L 560 340 L -20 340 Z" fill="var(--swoosh)"/>
      <path d="M180 -20 C 260 120, 300 220, 260 340" fill="none" stroke="var(--swoosh)" stroke-width="40"/>
    </svg>
    <div class="brand">
      <span class="brand__mark"></span>
      <span class="brand__name">VERDANT LOOP ADVISORS, LLC</span>
    </div>
  </section>

  <section class="card card--back" aria-label="Card back">
    <svg class="card__swooshes" viewBox="0 0 520 320" aria-hidden="true">
      <path d="M-20 250 C 140 160, 330 120, 560 170 L 560 -20 L -20 -20 Z" fill="var(--swoosh-on-white)"/>
      <path d="M300 -20 C 380 100, 420 220, 380 340" fill="none" stroke="var(--swoosh-on-white)" stroke-width="36"/>
    </svg>
    <div class="web-band">
      <span class="web-band__url">www.verdantloopadvisors.example</span>
    </div>
    <address class="contact">
      <p class="contact__address">5374 Tillbury Fenwood Road<br>Hyattsville, MD 20785</p>
      <p class="contact__phones">Tel.: 240.555.0143 Fax: 240.555.0187</p>
      <p class="contact__email">Email: sales@verdantloopadvisors.example</p>
    </address>
  </section>

</main>
</body>
</html>
```